Hello there!
I am looking to have a label created for a jojoba oil product I am launching. I have attached the logo of my company below. The label should have the following information on it as well:
Ingredients: pure jojoba oil
Size of the bottle: 118ml
And there might be more but I am working on this and will keep you posted.

```html
<!DOCTYPE html>
<html lang="en">
<head>
<meta charset="UTF-8">
<title>Pure Jojoba Oil – Label Designs</title>
<link href="https://fonts.googleapis.com/css2?family=Montserrat:wght@400;500;700&display=swap" rel="stylesheet">
<style>
  :root {
    --canvas: #ffffff;
    --ink-dark: #000000;
    --ink-light: #ffffff;
    --paper: #f2f2f0;
    --paper-edge: #e4e4e1;
  }
  * { margin: 0; padding: 0; box-sizing: border-box; }
  html, body {
    width: 960px;
    height: 1200px;
    overflow: hidden;
    background: var(--canvas);
    font-family: "Montserrat", sans-serif;
  }
  .label-sheet {
    position: relative;
    width: 960px;
    height: 1200px;
  }
  .label {
    position: absolute;
    top: 365px;
    width: 420px;
    height: 470px;
    text-align: center;
  }
  .label--dark { left: 40px; background: var(--ink-dark); color: var(--ink-light); }
  .label--light { left: 500px; background: var(--paper); color: var(--ink-dark); outline: 1px solid var(--paper-edge); }

  .label__brand {
    position: absolute;
    top: 44px;
    left: 53px;
    right: 53px;
    font-size: 27px;
    font-weight: 500;
    letter-spacing: 0.14em;
    line-height: 1.25;
  }
  .label__title {
    position: absolute;
    top: 182px;
    left: 0;
    right: 0;
    font-size: 44px;
    font-weight: 700;
    line-height: 1.02;
    letter-spacing: 0.02em;
  }
  .label__benefits {
    position: absolute;
    top: 298px;
    left: 53px;
    right: 53px;
    height: 80px;
    border-top: 2px solid currentColor;
    border-bottom: 2px solid currentColor;
    list-style: none;
    padding-top: 7px;
    font-size: 18px;
    font-weight: 400;
    line-height: 22px;
    letter-spacing: 0.03em;
  }
  .label__size {
    position: absolute;
    top: 414px;
    left: 0;
    right: 0;
    font-size: 21px;
    font-weight: 500;
  }
</style>
</head>
<body>
<main class="label-sheet">
  <section class="label label--dark">
    <p class="label__brand">MEADOWLARK<br>HAIR ATELIER</p>
    <h1 class="label__title">PURE<br>JOJOBA OIL</h1>
    <ul class="label__benefits">
      <li>HYDRATES SKIN</li>
      <li>ANTI-AGING</li>
      <li>HAIR HEALTH</li>
    </ul>
    <p class="label__size">118ml/4 oz</p>
  </section>

  <section class="label label--light">
    <p class="label__brand">MEADOWLARK<br>HAIR ATELIER</p>
    <h2 class="label__title">PURE<br>JOJOBA OIL</h2>
    <ul class="label__benefits">
      <li>HYDRATES SKIN</li>
      <li>ANTI-AGING</li>
      <li>HAIR HEALTH</li>
    </ul>
    <p class="label__size">118ml/4 oz</p>
  </section>
</main>
</body>
</html>
```